Website for Swedish wellness company "Heartmeadow"

We need a website for our Swedish wellness company. The name is "Heartmeadow" . The company is all about sustainablility for our body, soul and planet. We work with coaching, yoga, massage, healthy food, retreats(sports, excercise, sufing), healing and inspirational talks. We are convinced that personal sustainability and a strong spiritual connection to yourself will lead to planetary sustainability. Our customers are both companies and consumers from all over the world. The final design should be clean/simple and you should get a feeling of community, happiness, warmth, connection,, joy, spirituality but still a professional touch.Just got a logo from Pixel Harbor and are very happy with it;-)
Updates

Sorry I was too enthusiastic posting this project. Of course I will give you some text as well för the different pages! I will see to that it is finished by friday so if you want to wait with your submissions please do! Best regards Maria

Target Market(s)

Businesses and consumers

Industry/Entity Type

Health And Wellness

Number of Pages Required

5+ page

Font styles to use
Sans Serif

Colors
33a6d7
00a990
b7a5cd

Requirements
Must have
• Idea about pages:
• I am not sure how many pages I get for the price, but 5 would be nice to start with.
• Not sure what write ups is;-)
• But title of the pages could be:
• Landing page
• About us
• Services
• Retreats
• Contact us
Nice to have
• A clean and professional website but with some heart and soul in it. Because we Would love colours that harmonize with our logo, but other ideas are welcome!

```html
<!DOCTYPE html>
<html lang="en">
<head>
<meta charset="utf-8">
<title>Heartmeadow</title>
<link href="https://fonts.googleapis.com/css2?family=Montserrat:ital,wght@0,400;0,500;0,600;1,400;1,500&display=swap" rel="stylesheet">
<style>
:root{
  --teal:#62c9c9;
  --teal-text:#4fc3c3;
  --navy:#173a6e;
  --ink:#2a2a2a;
  --muted:#6b6b6b;
  --footer:#3d3d3d;
  --backdrop:#cdd1d4;
  --white:#ffffff;
}
*{margin:0;padding:0;box-sizing:border-box}
html,body{width:1200px;height:1200px;overflow:hidden}
body{background:radial-gradient(circle at 50% 45%,#e3e6e8 0%,var(--backdrop) 75%);font-family:'Montserrat',sans-serif;position:relative}
.page{position:absolute;left:230px;top:16px;width:740px;height:1168px;background:var(--white)}
.abs{position:absolute}
.topbar{left:45px;top:0;width:650px;height:18px;background:var(--teal)}
.social{right:6px;top:6px;display:flex;gap:4px}
.social span{width:6px;height:6px;border-radius:50%;background:var(--white)}
.nav{top:37px;font-size:8px;font-weight:500;color:var(--ink);letter-spacing:.2px}
.nav.active{color:var(--teal-text)}
.logo-box{left:56px;top:66px;width:163px;height:58px;background:var(--white);z-index:2;display:flex;flex-direction:column;align-items:center;justify-content:flex-end;padding-bottom:10px}
.logo-dot{width:34px;height:34px;border-radius:50%;background:var(--teal);margin-bottom:8px;position:absolute;top:-36px}
.logo-name{font-size:15px;font-weight:500;color:var(--navy);letter-spacing:.3px}
.hero{left:0;top:66px;width:740px;height:272px;background:linear-gradient(100deg,#8fb9d4 0%,#cfd9b6 22%,#f6d98a 45%,#e8a955 60%,#7c7f5a 80%,#5b5846 100%)}
.arrow{top:105px}
.cap-title{left:56px;top:172px;width:307px;height:27px;background:var(--teal);color:var(--white);font-size:10.5px;font-weight:500;display:flex;align-items:center;padding-left:14px;letter-spacing:.2px}
.cap-sub{left:56px;top:199px;width:307px;height:19px;background:var(--navy);color:var(--white);font-size:7.5px;font-style:italic;display:flex;align-items:center;justify-content:center}
.intro-h{left:0;top:380px;width:740px;text-align:center;color:var(--teal-text);font-size:16.5px;font-weight:600}
.intro-s{left:0;top:404px;width:740px;text-align:center;color:var(--ink);font-size:11.5px;font-style:italic;font-weight:500}
.card{width:190px;height:210px}
.card h3{font-size:9.5px;font-weight:600;color:var(--navy);padding-bottom:4px;border-bottom:1px solid var(--navy);margin-bottom:5px;height:12px;box-sizing:content-box}
.card .photo{width:190px;height:110px}
.card p{margin-top:12px;font-size:7.5px;line-height:10.5px;color:var(--muted);text-align:justify;letter-spacing:.2px}
.card .btn{position:absolute;left:0;top:186px;width:190px;height:24px;background:var(--teal);color:var(--white);font-size:9px;display:flex;align-items:center;justify-content:center}
.footer{left:45px;top:954px;width:650px;height:214px;background:var(--footer);color:var(--white)}
.f-small{top:41px;font-size:7px;font-weight:500}
.f-brand{left:0;width:650px;top:22px;display:flex;flex-direction:column;align-items:center}
.f-dot{width:30px;height:30px;border-radius:50%;border:1.5px solid var(--white);margin-bottom:4px}
.f-name{font-size:12px;font-weight:500;letter-spacing:.3px}
.f-rule{left:20px;top:84px;width:610px;height:1px;background:#cfcfcf}
.f-label{color:var(--teal-text);font-size:9.5px}
.f-val{font-size:9.5px}
.f-links{right:20px;top:124px;text-align:right;font-size:7px;line-height:10.2px}
.copy{left:0;width:650px;top:194px;text-align:center;font-size:7px;letter-spacing:2px;color:#6a6a6a}
</style>
</head>
<body>
<div class="page">
  <div class="abs topbar"><div class="abs social"><span></span><span></span><span></span></div></div>

  <div class="abs nav active" style="left:238px">HOME</div>
  <div class="abs nav" style="left:304px">ABOUT US</div>
  <div class="abs nav" style="left:386px">SERVICES</div>
  <div class="abs nav" style="left:466px">RETREATS</div>
  <div class="abs nav" style="left:548px">HEALTH TIPS</div>
  <div class="abs nav" style="left:642px">CONTACT US</div>

  <div class="abs hero" role="img" aria-label="Runner's feet on a sunlit country road with trees and low sun"></div>
  <div class="abs logo-box"><span class="logo-dot"></span><span class="logo-name">HEARTMEADOW</span></div>
  <svg class="abs arrow" style="left:60px" width="14" height="26" viewBox="0 0 14 26"><path d="M12 2 L2 13 L12 24" fill="none" stroke="#fff" stroke-width="2"/></svg>
  <svg class="abs arrow" style="left:667px" width="14" height="26" viewBox="0 0 14 26"><path d="M2 2 L12 13 L2 24" fill="none" stroke="#fff" stroke-width="2"/></svg>
  <div class="abs cap-title">LOREM IPSUM IS SIMPLY DUMMY TEXT OF PRINTING</div>
  <div class="abs cap-sub">It is a long established fact that a reader will be distracted by the</div>

  <div class="abs intro-h">There are many variations of passages of Lorem Ipsum opposed</div>
  <div class="abs intro-s">It is a long established fact that a reader will be distracted by the readable content of a page</div>

  <div class="abs card" style="left:58px;top:445px"><h3>STRESS</h3><div class="photo" role="img" aria-label="Tired man at a laptop rubbing his eyes" style="background:linear-gradient(120deg,#e9eef2,#9fb3c4 60%,#4d6478)"></div><p>There are many variations of passages of available, but the majority have suffered alteration in some form.</p><div class="btn">Read More About Stress</div></div>
  <div class="abs card" style="left:275px;top:445px"><h3>COLDS &amp; FLU</h3><div class="photo" role="img" aria-label="Woman with a cold lying under a blanket holding a tissue" style="background:linear-gradient(120deg,#d9cfc4,#a88f7c 55%,#e9e3dc)"></div><p>There are many variations of passages of available, but the majority have suffered alteration in some form.</p><div class="btn">Read More About Colds &amp; Flu</div></div>
  <div class="abs card" style="left:491px;top:445px"><h3>RELATIONSHIPS</h3><div class="photo" role="img" aria-label="Couple sitting apart outdoors after an argument" style="background:linear-gradient(120deg,#6f7d4e,#b9a48c 40%,#2e3548 75%,#5f6b55)"></div><p>There are many variations of passages of available, but the majority have suffered alteration in some form.</p><div class="btn">Read More About Relationships</div></div>

  <div class="abs card" style="left:58px;top:696px"><h3>NUTRITION</h3><div class="photo" role="img" aria-label="Woman eating a fresh salad at a table with vegetables" style="background:linear-gradient(120deg,#e8e2d6,#7c9ab3 45%,#8aa35a 75%,#d8cfbf)"></div><p>There are many variations of passages of available, but the majority have suffered alteration in some form.</p><div class="btn">Read More About Nutrition</div></div>
  <div class="abs card" style="left:275px;top:696px"><h3>SEXUAL HEALTH COMMUNICATION</h3><div class="photo" role="img" aria-label="Counselling session with hands and a clipboard" style="background:linear-gradient(120deg,#3c4a5c,#8a5a4e 45%,#f1c9b4 75%,#f6ede6)"></div><p>There are many variations of passages of available, but the majority have suffered alteration in some form.</p><div class="btn">Read More About Sexual health</div></div>
  <div class="abs card" style="left:491px;top:696px"><h3>SLEEPING WELL</h3><div class="photo" role="img" aria-label="Woman sleeping peacefully on white pillows" style="background:linear-gradient(120deg,#f3f1ef,#d9d4cf 50%,#a98b78 70%,#efe9e4)"></div><p>There are many variations of passages of available, but the majority have suffered alteration in some form.</p><div class="btn">Read More About Sleeping Well</div></div>

  <div class="abs footer">
    <div class="abs f-small" style="left:20px">Lorem Ipsum is simply dummy text</div>
    <div class="abs f-brand"><span class="f-dot"></span><span class="f-name">HEARTMEADOW</span></div>
    <div class="abs f-small" style="right:21px">printing and typesetting industry</div>
    <div class="abs f-rule"></div>
    <div class="abs" style="left:20px;top:124px;line-height:16.6px">
      <div class="f-label">Telephone</div><div class="f-val">01 48 22 71 36</div>
      <div class="f-label">Email</div><div class="f-val">hello@heartmeadow-mail.com</div>
    </div>
    <div class="abs" style="left:0;width:650px;top:124px;text-align:center;line-height:16.6px">
      <div class="f-label">HEARTMEADOW</div>
      <div style="font-size:8px">Your Address Line Goes Here 1,</div>
      <div style="font-size:8px">Adress Line 2 Goes here, Adress Line 2 Goes Here</div>
    </div>
    <div class="abs f-label" style="right:20px;top:124px;line-height:16.6px">Quick access</div>
    <div class="abs f-links" style="top:142px"><div>About us</div><div>Services</div><div>Retreats</div><div>Health Tips</div><div>Contact us</div></div>
    <div class="abs copy">Copyright © 2016 HEARTMEADOW</div>
  </div>
</div>
</body>
</html>
```